Brochure Design Project

We need a brochure designed for our company, specifically targeted at our corporate business customers ... Banks, Financial Services, Government. The brochure needs to detail our services and what we have to offer.

It may be a brochure/booklet that we can give to clients when we meet them. It needs to have a very corporate look and feel and needs to align with our colour palette and logo.

Information is held on our website www.tessaroworldservices.com
Updates

Thank you everyone for being part of this project.  It was a very hard decision.

Target Market(s)

Corporate business and clients including banks, financial services, insurance and government.

Industry/Entity Type

Business

Requirements
Must have
• Must have a corporate and global feel to it.
Must have our logo and same or similar colour palette.

```html
<!DOCTYPE html>
<html lang="en">
<head>
<meta charset="utf-8">
<title>Tessaro World Services – Brochure</title>
<link href="https://fonts.googleapis.com/css2?family=Source+Sans+3:ital,wght@0,400;0,600;0,700;1,400;1,600;1,700&display=swap" rel="stylesheet">
<style>
:root{
  --navy:#18265f;
  --navy-deep:#0f1a4a;
  --royal:#1d4fa6;
  --bright:#2c6fd1;
  --sky:#5b9ae6;
  --head-blue:#1f4d9e;
  --ink:#5a5a5a;
  --ink-dark:#333;
  --paper:#ffffff;
  --canvas:#ffffff;
  --label:#222;
}
*{box-sizing:border-box;margin:0;padding:0}
html,body{width:849px;height:1200px;overflow:hidden;background:var(--canvas)}
body{font-family:"Source Sans 3",Arial,sans-serif;color:var(--ink)}
.stage{position:absolute;left:0;top:0;width:906px;height:1280px;transform:scale(.9371);transform-origin:0 0}
.abs{position:absolute}
.label{font-size:12px;color:var(--label);font-weight:400}
.spread{position:absolute;box-shadow:0 2px 8px rgba(0,0,0,.35);background:var(--paper);overflow:hidden}

/* ---- outer spread ---- */
.outer{left:55px;top:72px;width:794px;height:560px}
.back-hero{left:0;top:0;width:397px;height:260px;background:radial-gradient(circle at 25% 25%,#3d7fd8 0,#1b3f8c 35%,#0c1d52 75%)}
.solutions-title{left:60px;top:54px;color:#fff;font-weight:600;font-size:11px;letter-spacing:.2px}
.sol-box{position:absolute;width:105px;height:103px;border-radius:9px;background:rgba(37,96,190,.78);padding:9px 7px;color:#fff}
.sol-box h3{font-size:7.8px;font-weight:600;line-height:1.25;margin-bottom:9px;text-transform:uppercase}
.sol-box p{font-size:6.6px;line-height:1.3;color:#dbe6fa}
.clients{left:31px;top:275px;color:var(--royal)}
.clients .small{font-size:10px;font-weight:700}
.clients .big{font-size:20px;font-weight:700;line-height:1}
.quote{position:absolute;font-size:6.7px;line-height:1.3;color:var(--ink)}
.quote.ruled{border-left:1px solid #c9c9c9;padding-left:6px}
.band{left:0;top:376px;width:794px;height:32px;background:linear-gradient(90deg,var(--navy-deep),var(--royal) 55%,var(--navy-deep))}
.brand{display:flex;align-items:center;gap:6px;color:var(--navy);font-weight:700;font-size:12px;line-height:1.05;text-transform:uppercase;letter-spacing:.3px}
.brand-dot{width:22px;height:22px;border-radius:50%;background:var(--royal);flex:none}
.social{left:151px;top:466px;display:flex;gap:5px}
.social span{width:20px;height:20px;border-radius:3px;background:var(--royal)}
.contact{left:152px;top:494px;font-size:6.7px;line-height:1.35;color:var(--ink-dark)}
.contact b{font-weight:700}
.fold{left:397px;top:0;width:1px;height:560px;background:#d8d8d8}
.cover-top{left:397px;top:0;width:397px;height:408px;background:linear-gradient(160deg,#1f3a8a 0,var(--navy) 45%,var(--navy-deep) 100%)}
.cover-photo{left:410px;top:118px;width:384px;height:216px;border-radius:120px 0 0 120px;background:radial-gradient(circle at 18% 45%,#cfe0f7 0,#6f9be0 18%,#2e5fb5 40%,#6d8dc7 70%,#d6deef 100%)}
.cover-title{left:440px;top:355px;color:#fff;font-size:15px;line-height:1.2;font-weight:400}
.cover-title b{font-weight:700;font-size:14px}

/* ---- inside spread ---- */
.inner{left:55px;top:675px;width:794px;height:562px}
.intro-panel{left:0;top:0;width:237px;height:562px;background:linear-gradient(180deg,var(--navy) 0,#1d2f78 60%,var(--navy-deep))}
.intro-panel .lead{position:absolute;left:34px;top:90px;width:185px;font-size:12px;line-height:1.3;color:var(--sky)}
.intro-panel .lead b{font-weight:700}
.body-white{position:absolute;left:34px;width:190px;font-size:7.3px;line-height:1.33;color:#fff;font-weight:600}
.body-white p{margin-bottom:8px}
.panel-head{position:absolute;font-size:12px;font-weight:600;color:var(--sky);letter-spacing:.3px}
.team-photo{left:237px;top:0;width:160px;height:285px;background:linear-gradient(180deg,#eef2fa 0,#aebfe0 45%,#5677b8 100%)}
.values{left:237px;top:285px;width:160px;height:277px;background:linear-gradient(180deg,var(--bright),var(--royal))}
.values .panel-head{left:14px;top:8px;color:#fff}
.values ul{position:absolute;left:14px;top:32px;width:135px;list-style:none;color:#fff;font-style:italic;font-weight:700;font-size:7.6px;line-height:1.35}
.values li{margin-bottom:12px}
.services-photo{left:397px;top:0;width:397px;height:152px;overflow:hidden}
.services-title{left:424px;top:62px;color:#fff;font-weight:600;font-size:12px;text-shadow:0 1px 2px rgba(0,0,0,.3);z-index:2}
.col{position:absolute;top:168px;width:155px;font-size:6.8px;line-height:1.32;color:var(--ink)}
.col h4{font-size:7.4px;color:var(--head-blue);font-weight:700;text-transform:uppercase;margin:8px 0 7px}
.col h4:first-child{margin-top:0}
.col h5{font-size:10px;color:var(--ink-dark);font-weight:400;line-height:1.1;margin:-4px 0 7px}
.col p{margin-bottom:6px;text-align:justify}
.col .accent{color:var(--bright);font-weight:700}
</style>
</head>
<body>
<div class="stage">
  <div class="abs label" style="left:55px;top:34px">Back cover</div>
  <div class="abs label" style="left:452px;top:34px">cover</div>
  <div class="abs label" style="left:55px;top:649px">Inside spread</div>

  <!-- Outer spread: back cover + cover -->
  <section class="spread outer">
    <div class="abs back-hero" role="img" aria-label="Photo of a glowing light bulb containing a world globe on a deep blue background"></div>
    <div class="abs solutions-title">OUR SOLUTIONS</div>
    <div class="sol-box" style="left:147px;top:35px"><h3>Banking &amp; Finance Solutions</h3><p>With extensive experience in banking and financial services our models and solutions are designed specifically to support the needs of this industry ensuring sustainable results.</p></div>
    <div class="sol-box" style="left:258px;top:35px"><h3>Business Solutions</h3><p>Whether you are optimising or transforming an existing business or creating something totally new we can assist.</p></div>
    <div class="sol-box" style="left:35px;top:142px"><h3>Community Solutions</h3><p>Dealing with all aspects of the community including mental health, homelessness, juvenile, welfare, judicial, indigenous, eldery and many others.</p></div>
    <div class="sol-box" style="left:147px;top:142px"><h3>Environmental Solutions</h3><p>To create sustainable solutions all aspects of the Environmental system need to be understood and managed as a ‘whole’ system.</p></div>
    <div class="sol-box" style="left:258px;top:142px"><h3>Global Solutions</h3><p>TWS specialise in working with complex problems that are multi-layered and have multiple interdependencies.</p></div>

    <div class="abs clients"><div class="small">WHAT OUR</div><div class="big">clients say ...</div></div>
    <p class="quote" style="left:31px;top:316px;width:76px">“Put simply TWS helps companies remediate critical, and in many cases intractable problems”</p>
    <p class="quote ruled" style="left:109px;top:316px;width:82px">“From Re-engineering to “Sustainable” Transformation and change, TWS can help find a way forward through the most complex blockers.”</p>
    <p class="quote ruled" style="left:195px;top:280px;width:82px">“TWS have become the ‘go to’ practitioners that organisations call upon when they need a remedy and they need it fast! They have an ability to cut through complexity and provide clarity on the way forward quickly and efficiently.”</p>
    <p class="quote ruled" style="left:281px;top:280px;width:84px">“We wanted to transform our Organisation but were unsure of how to bring it all together. TWS supported us in creating a clear path forward managing all the moving parts. The result has been first class!”</p>

    <div class="abs cover-top"></div>
    <div class="abs band"></div>
    <div class="abs cover-photo" role="img" aria-label="Photo of a glass globe with a stethoscope and a hand on a computer mouse"></div>
    <div class="abs cover-title">Specialists in <b>Transformational Change</b><br>&amp; <b>Sustainable Solutions</b></div>

    <div class="abs brand" style="left:30px;top:470px;width:110px"><span class="brand-dot"></span><span>Tessaro World Services</span></div>
    <div class="abs social"><span></span><span></span><span></span></div>
    <div class="abs contact">Tessaro World Services Pty Ltd<br>PO Box 41, Harbour Street West, Victoria 8010, AUSTRALIA<br>Tel: +61 (03) 9000 4821 - info@tessaroworldservices.com<br><b>www.tessaroworldservices.com</b></div>

    <div class="abs brand" style="left:648px;top:455px;width:120px"><span class="brand-dot"></span><span>Tessaro World Services</span></div>
    <div class="abs fold"></div>
  </section>

  <!-- Inside spread -->
  <section class="spread inner">
    <div class="abs intro-panel">
      <div class="lead">Specialists in <b>Transformational Change</b> &amp; <b>Sustainable Solutions</b></div>
      <div class="body-white" style="top:140px">
        <p>To succeed in an increasingly competitive and rapidly changing global market and envrionment, a new way of thinking and design is required.</p>
        <p>Tessaro World Services brings a dynamic and leading edge approach to support our clients needs. We work across a broad sector supporting the changes required to excel in the 21st Century.</p>
        <p>We believe in partnering with our clients to develop sustainable solutions that support transition from the current state to the future state.</p>
      </div>
      <div class="panel-head" style="left:34px;top:294px">OUR TEAM</div>
      <div class="body-white" style="top:326px">
        <p>The Team from Tessaro World Services have a broad range of experience across all aspects of business and community. They are specifically qualified and trained in all aspects of Solution design as required by both TWS and our clients alike.</p>
        <p>The Executive team have over 40 years experience across major corporates, government as well as the health and wellness industries.</p>
        <p>Our approach draws from our own extensive experience whilst integrating many well known disciplines such as quantum physics, energetic and informational medicine, sociology, psychotherapy, neuro-linguistic programming, bioenergetics and systems thinking.</p>
      </div>
    </div>
    <div class="abs team-photo" role="img" aria-label="Photo of a team holding up jigsaw puzzle pieces against the sky"></div>
    <div class="abs values">
      <div class="panel-head">OUR VALUES</div>
      <ul>
        <li>“We act with integrity”</li>
        <li>We are innovative<br>and creative.</li>
        <li>We design sustainable solutions for our future generations.</li>
        <li>We believe sustainable solutions are the only answer and all our work is built with this central premise in mind.</li>
        <li>We believe in collaboration.</li>
      </ul>
    </div>

    <svg class="abs services-photo" viewBox="0 0 397 152" role="img" aria-label="Photo of a business handshake in front of glass office towers">
      <defs>
        <linearGradient id="handshakeTones" x1="0" y1="0" x2="1" y2="1">
          <stop offset="0" stop-color="#2a4fa3"/>
          <stop offset=".45" stop-color="#9fb6de"/>
          <stop offset=".7" stop-color="#e3c9b8"/>
          <stop offset="1" stop-color="#3d6bc0"/>
        </linearGradient>
        <linearGradient id="towerTones" x1="0" y1="0" x2="0" y2="1">
          <stop offset="0" stop-color="#8fb0e6"/>
          <stop offset="1" stop-color="#2a57b0"/>
        </linearGradient>
      </defs>
      <rect width="397" height="152" fill="#fff"/>
      <ellipse cx="190" cy="-40" rx="232" ry="186" fill="url(#handshakeTones)"/>
      <path d="M366 0 H397 V128 C380 142 356 150 330 152 C368 112 380 56 366 0 Z" fill="url(#towerTones)"/>
    </svg>
    <div class="abs services-title">OUR SERVICES</div>

    <div class="col" style="left:431px">
      <h4>Trouble Shooting</h4>
      <p>Whether designing or re-engineering we support all facets of business development using leading edge models and thinking. We work with your business to understand, measure and analyse problems. We develop sustainable solutions to address the root cause of a problem or an issue and align these solutions to your organisational strategy. We ensure the solution focuses on “speed to value” creating early realisation of benefits and facilitating delivery of the business outcomes.</p>
      <h4>Strategy and Design</h4>
      <h5>Leading Edge Strategy &amp; Design</h5>
      <p>We believe in bringing a totally new approach to all that we do. Our design work uses leading edge models which take a multi-dimensional view of the business. Using the Arcus Model™ and Wave Dynamics™ ensures that a unique approach and a unique solution is designed for all our clients. We support all elements of strategic development and design.</p>
      <h4>Business Development</h4>
      <p>Whether designing or re-engineering we support all facets of business development using leading edge models and thinking. We work with your business to understand, measure and analyse problems. We develop sustainable solutions to address the root cause of a problem or an issue and align these solutions to your organisational strategy. We ensure the solution focuses on “speed to value” creating early realisation of benefits and facilitating delivery of the business outcomes.</p>
      <h4>Transformational Change</h4>
      <p>Using the latest thinking we partner with our clients to develop programs that support transformation to the desired state. We believe organisational &amp; cultural change</p>
    </div>
    <div class="col" style="left:599px;top:158px">
      <p>has to encompass the entire system the organisation sits in and use our FourPoint Change™ model combined with the unique client needs to embed a sustainable solution.</p>
      <h4>Project Management</h4>
      <p>Tessaro World Services utilises strong project management methodology. We are able to manage all aspects of the project, including all change management from current state to future state.</p>
      <h4>Coaching &amp; Team Dynamics</h4>
      <h5>Executive Coaching &amp;<br>Team Effectiveness</h5>
      <p class="accent">An Executive Coach can help you unlock your fully potential and help you get to where you want to be.</p>
      <p>TWS Executive Individual and Team Coaching is a world-class best practice initiative that provides businesses and individuals’ assistance in shaping transformative performance. Executive Coaching targets leadership development, improved business results and personal development goals. Executive Team Effectiveness targets team cohesion, team high performance and operating practices.</p>
      <h4>Leadership Development</h4>
      <p>Executive Coaching for Individuals &amp; Executive Team Effectiveness. An Executive Coach can help you unlock your fully potential and help you get to where you want to be. TWS Executive Individual and Team Coaching is a world-class best practice initiative that provides businesses and individuals’ assistance in shaping transformative performance. Executive Coaching targets leadership development, improved business results and personal development goals</p>
    </div>
  </section>
</div>
</body>
</html>
```